Manuka honey jar label for new Manuka brand

We are planning to start a Manuka honey brand and we need to design the label for the honey jar. Manuka honey is an up and coming product and the market is still young in our country.
Our market is dominated by 1 brand: Korivo Vital (photo attached). To the people who know what Manuka honey is, they associate it with Korivo Vital in the same way people associate Cola with Zibo Zesta or printer copies with Pluvex.
The good news is that a lot of people do not know yet what Manuka honey is and we still have the opportunity of being the first brand they get to know. At the same time, we still need to be able to take at least a bite out of the Korivo Vital market share.
The Korivo Vital label for their jar I think is not just absolutely gorgeous but it also does its job extremely well. It only features 3 informations:
- name of brand/logo (Korivo Vital)
- name of product (Manuka Honey)
- and mgo rating which is like a rating of how strong the honey is
By having just this information on a relatively small label, their label SCREAMS Manuka by having the Manuka words twice (the brand and the product name) and people develop this association between Korivo Vital and Manuka products in general.
Our product will also be in a similar square plastic jar. It will also be dark tinted, that´s important to note. We can also go for a blue cap but in order to differentiate ourselves from Korivo Vital we thought of maybe choosing a black lid instead. I uploaded 2 jars, 1 with black lid and 1 with gold (although it looks more like mustard) that you can use for simulations. They are pretty accurate of the type of jars and lids that we can have.
The label has total length of about 20cm. One side of the jar has 5,5 cm of the label and the height of the label is 4,5 cm. We can also use selective gold laminating on the label but we cannot have custom shape label at this point as Korivo Vital does with its tree logo that sticks outside the label.
I need the design for the entire label but the focus should be on the front part, that is the part that sells and catches your eye. Like Korivo Vital, the front part I want to have 3 vital informations:
- name of brand/logo (in our case Halvern Terra) - we do not have a pre-existing logo, this needs to be created alongside the label
- and mgo rating
As "other" information we also need the net weight "250 g" alongside with the typical "e" to appear on the front. That is a legal requirement.
Optionally, you can add a small phrase somewhere like "Harvested in New Zealand" or "Made in New Zealand" since this is a product that is only made there and in some areas of Australia.
This is pretty much all the info. As a final note, there are a ton of beautiful premium Manuka honey jar labels. But they are too fancy and when you look at them you don´t instantly recognize that it is Manuka Honey.
This instant recognition is vital! With this small jar there is the danger for customers to think that maybe it´s medicine, maybe it´s sports supplements etc. This is a relatively small product and imagine you just glance on it on the retail shelf. Instantly you must think it is Manuka Honey and that it is beautiful. And if you see it on the shelf next to Korivo Vital, it would be best to also think that you would rather buy this (it gives you more trust) than the Korivo Vital.
One final note: I do not want the bee as an insect on the label. I think some people are turned off when they see an insect with its small legs and make a bad association that there are insects inside. I do not mind symbolism or somehow super stylized bee in a modern way, but I do not want a plain insect on the label.
For any other questions, I am at your disposal. Thank you very much for taking the time to send us a proposal!

```html
<!DOCTYPE html>
<html lang="en">
<head>
<meta charset="UTF-8">
<title>Halvern Terra — Mānuka Honey Label</title>
<link href="https://fonts.googleapis.com/css2?family=Marcellus&family=Montserrat:wght@600;700&display=swap" rel="stylesheet">
<style>
  :root {
    --backdrop: #c0c2c0;
    --label-black: #141414;
    --pattern-tone: #1d1d1d;
    --band-orange: #e8950f;
    --band-orange-deep: #d9800a;
    --gold-light: #e2ad2a;
    --gold-dark: #8a6410;
    --ink-dark: #111111;
    --text-light: #ececea;
    --brand-gold: #d99a1c;
  }
  * { margin: 0; padding: 0; box-sizing: border-box; }
  html, body { width: 1200px; height: 908px; overflow: hidden; }
  body {
    background: var(--backdrop);
    position: relative;
    font-family: "Montserrat", sans-serif;
  }
  .label {
    position: absolute;
    left: 140px;
    top: 95px;
    width: 920px;
    height: 718px;
    background: var(--label-black);
    overflow: hidden;
  }
  .label__pattern {
    position: absolute;
    inset: 0;
    background: linear-gradient(120deg, var(--pattern-tone) 0%, var(--label-black) 55%, var(--pattern-tone) 100%);
  }
  .brand-band {
    position: absolute;
    left: 66px;
    top: 0;
    width: 150px;
    height: 100%;
    background: linear-gradient(90deg, var(--band-orange-deep), var(--band-orange));
    display: flex;
    align-items: center;
    justify-content: center;
  }
  .brand-band__name {
    transform: rotate(-90deg);
    white-space: nowrap;
    font-family: "Marcellus", serif;
    font-size: 86px;
    color: var(--ink-dark);
    letter-spacing: 1px;
  }
  .front {
    position: absolute;
    left: 216px;
    right: 0;
    top: 0;
    bottom: 0;
  }
  .brand-mark {
    position: absolute;
    left: 0;
    right: 0;
    top: 110px;
    text-align: center;
    font-family: "Marcellus", serif;
    font-size: 46px;
    color: var(--brand-gold);
    letter-spacing: 2px;
  }
  .product-name {
    position: absolute;
    left: 0;
    right: 0;
    top: 250px;
    text-align: center;
    font-family: "Marcellus", serif;
    font-size: 112px;
    line-height: 104px;
    color: var(--text-light);
  }
  .mgo-band {
    position: absolute;
    left: 30px;
    width: 609px;
    top: 511px;
    height: 83px;
    background: linear-gradient(90deg, var(--gold-dark) 0%, var(--gold-light) 45%, var(--gold-light) 60%, var(--gold-dark) 100%);
    display: flex;
    align-items: center;
    justify-content: center;
    font-weight: 700;
    font-size: 60px;
    color: var(--ink-dark);
    letter-spacing: 1px;
  }
  .meta-line {
    position: absolute;
    left: 0;
    right: 0;
    top: 628px;
    display: flex;
    align-items: center;
    justify-content: center;
    color: var(--text-light);
  }
  .meta-line__weight {
    font-weight: 700;
    font-size: 44px;
  }
  .meta-line__divider {
    width: 2px;
    height: 34px;
    background: var(--text-light);
    margin: 0 16px;
  }
  .meta-line__origin {
    font-weight: 600;
    font-size: 25px;
  }
</style>
</head>
<body>
  <div class="label">
    <div class="label__pattern" role="img" aria-label="Faint honeycomb pattern across the black label"></div>
    <div class="brand-band">
      <span class="brand-band__name">Halvern Terra</span>
    </div>
    <div class="front">
      <div class="brand-mark">Halvern Terra</div>
      <h1 class="product-name">Mānuka<br>Honey</h1>
      <div class="mgo-band">MGO 250+</div>
      <div class="meta-line">
        <span class="meta-line__weight">250g ℮</span>
        <span class="meta-line__divider"></span>
        <span class="meta-line__origin">MADE IN NEW ZEALAND</span>
      </div>
    </div>
  </div>
</body>
</html>
```